This is a label for a new sake made in Japan imported into Aust

This will be a bottle label for a new sake imported into Australia. The hero of the label is the Velmora. We have joined the "O" meaning great in Japanese and used sake with "Z" to have Velmora with the play on words using Oz as in our slang for Aussie. A modern label with a Japanese take is key. This is a premium sake made in Japan for the Australian market.
The "Tall Casks" up the top is the name of the company, we have yet to design a logo for the company.

Target Market(s)

Alcohol

Logo Text

Velmora

Font styles to use
Serif

Requirements
Must have
• easy to read, with a hint of Japanese origin
Should not have
• too busy

```html
<!DOCTYPE html>
<html lang="en">
<head>
<meta charset="utf-8">
<title>Velmora Sake Label</title>
<link rel="stylesheet" href="https://fonts.googleapis.com/css2?family=Cinzel:wght@400;700&family=Josefin+Sans:wght@600&display=swap">
<style>
  :root {
    --backdrop: #efefef;
    --paper: #f9f9f9;
    --indigo: #364a73;
    --ink: #1b1b1b;
    --mist: #e4e4e4;
  }
  * { margin: 0; padding: 0; box-sizing: border-box; }
  html, body {
    width: 1200px;
    height: 796px;
    overflow: hidden;
    background: var(--backdrop);
  }
  .canvas {
    position: relative;
    width: 1200px;
    height: 796px;
  }
  .label {
    position: absolute;
    left: 290px;
    top: 68px;
    width: 620px;
    height: 660px;
    background: var(--paper);
    box-shadow: 0 10px 40px rgba(0, 0, 0, 0.08);
    overflow: hidden;
  }
  .ink-wash {
    position: absolute;
    left: 440px;
    top: 94px;
    width: 180px;
    height: 404px;
    background: radial-gradient(ellipse at 70% 50%, var(--mist) 0%, rgba(228, 228, 228, 0.5) 45%, rgba(249, 249, 249, 0) 75%);
  }
  .company-mark {
    position: absolute;
    left: 284px;
    top: 46px;
    width: 52px;
    height: 52px;
    border: 4px solid var(--ink);
  }
  .company-name {
    position: absolute;
    top: 114px;
    left: 0;
    width: 100%;
    text-align: center;
    font-family: "Josefin Sans", sans-serif;
    font-weight: 600;
    font-size: 24px;
    letter-spacing: 0.42em;
    padding-left: 0.42em;
    color: var(--ink);
  }
  .product-name {
    position: absolute;
    top: 284px;
    left: 0;
    width: 100%;
    text-align: center;
    font-family: "Cinzel", serif;
    font-weight: 700;
    font-size: 96px;
    line-height: 1;
    color: var(--indigo);
  }
  .divider {
    position: absolute;
    top: 503px;
    left: 298px;
    width: 24px;
    height: 5px;
    background: var(--indigo);
  }
  .tagline {
    position: absolute;
    top: 528px;
    left: 0;
    width: 100%;
    text-align: center;
    font-family: "Cinzel", serif;
    font-weight: 400;
    font-size: 27px;
    line-height: 29px;
    letter-spacing: 0.14em;
    padding-left: 0.14em;
    color: var(--ink);
  }
  .base-band {
    position: absolute;
    left: 0;
    top: 621px;
    width: 100%;
    height: 14px;
    background: var(--indigo);
  }
</style>
</head>
<body>
  <main class="canvas">
    <section class="label">
      <div class="ink-wash" role="img" aria-label="Faint grey brush-ink decoration"></div>
      <div class="company-mark"></div>
      <p class="company-name">TALL CASKS</p>
      <h1 class="product-name">VELMORA</h1>
      <div class="divider"></div>
      <p class="tagline">PREMIUM<br>JAPANESE SAKE</p>
      <div class="base-band"></div>
    </section>
  </main>
</body>
</html>
```